Pipelining Product Supply Company Needs New Stationery

We need new stationery (letter head, with compliments slips & business card) for our industry leading pipe lining supply company. basically we sell product to other plumbers to carry out pipe relining.

Im looking for something, fresh, professional, sleek and modern at the same time.

Ive attached a copy of the logo and also some guidelines to follow for colours and fonts etc.

Target Market(s)

Plumbers

Industry/Entity Type

Plumbing

Font styles to use
Sans Serif

Requirements
Must have
• The logo, space for ABN, Address, Phone Number, website and email.
Nice to have
• Stand out from the crowd. To look sleep and professional.
Should not have
• Any other colours apart from what is on the guidelines.

```html
<!DOCTYPE html>
<html lang="en">
<head>
<meta charset="utf-8">
<title>Southern Reline Supplies – Business Card</title>
<link rel="stylesheet" href="https://fonts.googleapis.com/css2?family=Open+Sans:wght@400;600;700&display=swap">
<style>
  :root {
    --backdrop: #2b2b2b;
    --green-light: #8cc63f;
    --green-mid: #4f9a2a;
    --green-deep: #1d5f12;
    --card-white: #f4f4f4;
    --ink: #3d3d3d;
    --ink-soft: #8a8a8a;
    --rule: #c9c9c9;
  }
  * { margin: 0; padding: 0; box-sizing: border-box; }
  html, body {
    width: 1200px; height: 960px; overflow: hidden;
    background: var(--backdrop);
    font-family: "Open Sans", Arial, sans-serif;
  }
  .canvas { position: relative; width: 1200px; height: 960px; }

  .card { position: absolute; left: 320px; width: 600px; height: 344px; }

  /* Front */
  .card-front {
    top: 100px;
    background: radial-gradient(ellipse 55% 60% at 50% 50%, var(--green-light) 0%, var(--green-mid) 45%, var(--green-deep) 100%);
    display: flex; flex-direction: column; align-items: center; justify-content: center;
  }
  .brand-front {
    color: #ffffff; font-weight: 400; font-size: 28px; letter-spacing: 1px;
    text-transform: uppercase; text-align: center; line-height: 1.3;
    display: flex; align-items: center; gap: 14px;
    margin-top: 20px;
  }
  .brand-mark { width: 18px; height: 18px; background: #ffffff; flex: none; }

  /* Back */
  .card-back { top: 492px; background: var(--card-white); }
  .brand-back {
    position: absolute; left: 60px; top: 130px; width: 260px;
    color: var(--ink-soft); font-weight: 400; font-size: 22px;
    text-transform: uppercase; text-align: center; line-height: 1.3;
  }
  .divider {
    position: absolute; left: 330px; top: 88px; width: 1px; height: 165px;
    background: var(--rule);
  }
  .contact { position: absolute; left: 355px; top: 92px; color: var(--ink); }
  .contact-name { color: var(--green-light); font-weight: 600; font-size: 19px; line-height: 24px; }
  .contact-role { color: var(--ink-soft); font-size: 14px; line-height: 20px; text-transform: uppercase; }
  .contact-address { margin-top: 14px; font-size: 14px; line-height: 19px; }
  .contact-lines { margin-top: 8px; font-size: 14px; line-height: 19px; }
  .contact-line { display: flex; align-items: center; gap: 12px; }
  .contact-line svg { width: 14px; height: 12px; fill: var(--green-light); flex: none; }

  .web-band {
    position: absolute; left: 0; right: 0; top: 298px; height: 34px;
    border-top: 3px solid var(--rule); border-bottom: 3px solid var(--rule);
    background: linear-gradient(90deg, var(--green-deep) 0%, var(--green-mid) 50%, var(--green-deep) 100%);
    display: flex; align-items: center; justify-content: center;
  }
  .web-address { color: #ffffff; font-weight: 700; font-size: 14px; letter-spacing: 1px; }
</style>
</head>
<body>
<div class="canvas">
  <section class="card card-front">
    <div class="brand-front"><span class="brand-mark"></span><span>Southern Reline<br>Supplies</span></div>
  </section>

  <section class="card card-back">
    <div class="brand-back">Southern Reline<br>Supplies</div>
    <div class="divider"></div>
    <div class="contact">
      <div class="contact-name">TOBIN ASHCROFT</div>
      <div class="contact-role">President</div>
      <div class="contact-address">
        2710 Harbour Road Lane<br>
        Brookvale, NSW 2100<br>
        ABN: 4817902356
      </div>
      <div class="contact-lines">
        <div class="contact-line">
          <svg viewBox="0 0 14 12" aria-hidden="true"><path d="M1 3 Q7 -1 13 3 L11 5 L9 3.5 Q7 3 5 3.5 L3 5 Z M3 6 H11 L12 11 H2 Z"/></svg>
          <span>855 0147 2290</span>
        </div>
        <div class="contact-line">
          <svg viewBox="0 0 14 12" aria-hidden="true"><path d="M1 2 H13 V3 L7 7 L1 3 Z M1 4.5 L7 8.5 L13 4.5 V10 H1 Z"/></svg>
          <span>info@srsupplies.com</span>
        </div>
      </div>
    </div>
    <div class="web-band"><span class="web-address">www.southernrelinesupplies.com</span></div>
  </section>
</div>
</body>
</html>
```